Freelance Translator in Need of a Business Card

I am a freelance Japanese to English translator. I work in the video game localization industry and do literary translation in my spare time. I would like to have both the English word 'Translator' and the Japanese '翻訳者' in the job title. The final design should evoke trust, openness, and reliability.

Target Market(s)

Video game localization companies
Japanese comic book artists

Industry/Entity Type

Business

Contact Information for Business Card

Daniel Oskerby, Translator
dan.oskerby@fernlowmail.com
velmotranslates.com
twitter: @velmo_tl

Colors

Designer to choose colors to be used in the design.

```html
<!DOCTYPE html>
<html lang="en">
<head>
<meta charset="utf-8">
<title>Daniel Oskerby — Translator Business Card</title>
<link rel="stylesheet" href="https://fonts.googleapis.com/css2?family=Lato:wght@400;700&family=Quicksand:wght@400;700&family=Noto+Sans+JP:wght@400&display=swap">
<style>
  :root {
    --page-bg: #d9d9d9;
    --card-yellow: #e6ad34;
    --ink: #161616;
    --ink-soft: #2a2210;
    --card-black: #121212;
    --key-grey: #2c2c2c;
    --white: #f5f5f5;
    --photo-tone-dark: #3a2e12;
    --photo-tone-mid: #8a6a22;
  }
  * { margin: 0; padding: 0; box-sizing: border-box; }
  html, body {
    width: 1200px; height: 1200px; overflow: hidden;
    background: var(--page-bg);
  }
  .sheet {
    width: 1200px; height: 1200px;
    display: flex; flex-direction: column; align-items: center; justify-content: center;
    gap: 56px;
  }
  .card {
    position: relative;
    width: 900px; height: 514px;
    overflow: hidden;
    box-shadow: 0 6px 18px rgba(0,0,0,0.18);
  }

  /* Front */
  .card--front { background: var(--card-yellow); color: var(--ink); }
  .identity { position: absolute; left: 78px; top: 64px; }
  .identity__name {
    font-family: "Quicksand", sans-serif;
    font-size: 50px; line-height: 1; letter-spacing: 0.5px;
  }
  .identity__first { font-weight: 700; }
  .identity__last { font-weight: 400; }
  .identity__title {
    margin-top: 10px;
    font-family: "Lato", "Noto Sans JP", sans-serif;
    font-size: 25px; color: var(--ink-soft);
  }
  .identity__rule {
    margin-top: 8px; width: 160px; height: 3px; background: var(--ink);
  }
  .contact-list {
    position: absolute; left: 78px; top: 250px;
    list-style: none;
    font-family: "Lato", sans-serif; font-size: 26px; line-height: 38px;
  }
  .contact-list li { display: flex; align-items: center; gap: 12px; }
  .contact-list svg { width: 20px; height: 20px; flex: none; }
  .product-photo {
    position: absolute; left: 540px; top: 200px; width: 320px; height: 230px;
    background: radial-gradient(ellipse at 50% 55%, var(--photo-tone-dark) 0%, var(--photo-tone-mid) 60%, var(--card-yellow) 100%);
    border-radius: 8px;
  }

  /* Back */
  .card--back { background: var(--card-black); }
  .keyboard-photo {
    position: absolute; inset: 0;
    background: radial-gradient(ellipse at 40% 35%, var(--key-grey) 0%, var(--card-black) 70%);
  }
  .emblem {
    position: absolute; left: 310px; top: 70px; width: 280px; height: 280px;
    border-radius: 50%;
    background: var(--card-yellow);
    border: 4px solid var(--white);
    box-shadow: 0 0 0 6px var(--card-black);
  }
  .web-line {
    position: absolute; left: 0; right: 0; top: 410px;
    display: flex; align-items: center; gap: 18px;
  }
  .web-line__rule { flex: 1; height: 2px; background: var(--white); }
  .web-line__rule--short { flex: 0 0 250px; }
  .web-line__url {
    font-family: "Lato", sans-serif; font-size: 34px; color: var(--white);
    letter-spacing: 0.5px;
  }
</style>
</head>
<body>
<main class="sheet">
  <section class="card card--front">
    <div class="identity">
      <h1 class="identity__name"><span class="identity__first">Daniel</span> <span class="identity__last">Oskerby</span></h1>
      <p class="identity__title">Translator, 翻訳者</p>
      <div class="identity__rule"></div>
    </div>
    <ul class="contact-list">
      <li>
        <svg viewBox="0 0 20 20" aria-hidden="true"><path d="M3 6c0-2 2-3 7-3s7 1 7 3v2h-4V6H7v2H3z M5 9h10l2 8H3z" fill="currentColor"/></svg>
        555 014 2276
      </li>
      <li>
        <svg viewBox="0 0 20 20" aria-hidden="true"><rect x="2" y="5" width="16" height="11" fill="currentColor"/><path d="M2 5l8 6 8-6" stroke="#e6ad34" stroke-width="1.5" fill="none"/></svg>
        dan.oskerby@fernlowmail.com
      </li>
      <li>
        <svg viewBox="0 0 20 20" aria-hidden="true"><circle cx="10" cy="10" r="8" fill="currentColor"/><path d="M2 10h16M10 2c-4 4-4 12 0 16M10 2c4 4 4 12 0 16" stroke="#e6ad34" stroke-width="1.2" fill="none"/></svg>
        www.velmotranslates.com
      </li>
      <li>
        <svg viewBox="0 0 20 20" aria-hidden="true"><circle cx="10" cy="10" r="7" fill="currentColor"/></svg>
        @velmo_tl
      </li>
    </ul>
    <div class="product-photo" role="img" aria-label="Photograph of a vintage typewriter tinted in yellow and black"></div>
  </section>

  <section class="card card--back">
    <div class="keyboard-photo" role="img" aria-label="Dark blurred close-up photograph of keyboard keys"></div>
    <div class="emblem" role="img" aria-label="Illustration of an orange typewriter with a sheet of paper inside a yellow circle"></div>
    <div class="web-line">
      <span class="web-line__rule"></span>
      <span class="web-line__url">www.velmotranslates.com</span>
      <span class="web-line__rule web-line__rule--short"></span>
    </div>
  </section>
</main>
</body>
</html>
```